Vehicle Signage

Please design a graphic layout for a Van signage to advertise the business

"Kestrel Vantage Systems"
the logo is in the attached files

Also attached are some icons that represent the fields of service, I would like to use these in the design please
Updates

Reason: I am making some changes to the KVS logo to help match the Vans, I will up load the new files as soon as possible

Target Market(s)

We are targeting people who feel they would like to have some security equipment installed for piece of mind in the the fields of:
"Alarms, Intercoms, CCTV, Access Control"

Industry/Entity Type

Business

Requirements
Must have
• Must be Clear what we do,
it can be icons/pictures or words to represent the service areas of:

```html
<!DOCTYPE html>
<html lang="en">
<head>
<meta charset="utf-8">
<title>Kestrel Vantage Systems – Van Side Graphic</title>
<link rel="stylesheet" href="https://fonts.googleapis.com/css2?family=Exo+2:wght@700&display=swap">
<style>
  :root {
    --navy: #134a72;
    --blue: #1d6fa3;
    --blue-light: #2c8cc4;
    --orange: #f39a1b;
    --orange-deep: #e4721a;
    --white: #ffffff;
    --panel: #f4f5f6;
    --icon-dark: #3f454b;
    --icon-mid: #5c636a;
    --icon-line: #dfe3e6;
    --page: #e6e8ea;
  }
  * { margin: 0; padding: 0; box-sizing: border-box; }
  html, body { width: 1200px; height: 504px; overflow: hidden; background: var(--page); }
  .wrap-panel {
    position: relative;
    width: 1200px;
    height: 504px;
    font-family: "Exo 2", Arial, sans-serif;
    font-weight: 700;
  }
  .wrap-art { position: absolute; inset: 0; }
  .brand {
    position: absolute;
    left: 210px;
    top: 96px;
    color: var(--navy);
    line-height: 1;
    letter-spacing: 1px;
  }
  .brand-line-main { display: block; font-size: 50px; }
  .brand-line-sub { display: block; font-size: 30px; margin-top: 6px; letter-spacing: 2px; }
  .services {
    position: absolute;
    left: 714px;
    top: 262px;
    width: 240px;
    list-style: none;
    text-align: center;
    color: var(--white);
    font-size: 22px;
    line-height: 29px;
    letter-spacing: 0.5px;
  }
  .phone {
    position: absolute;
    left: 418px;
    top: 377px;
    color: var(--orange);
    font-size: 34px;
    letter-spacing: 0.5px;
  }
</style>
</head>
<body>
<main class="wrap-panel">
  <svg class="wrap-art" width="1200" height="504" viewBox="0 0 1200 504" aria-hidden="true">
    <defs>
      <linearGradient id="body-blue" x1="0" y1="0" x2="1" y2="1">
        <stop offset="0" stop-color="#1f7ab2"/>
        <stop offset="0.6" stop-color="#17578a"/>
        <stop offset="1" stop-color="#123f66"/>
      </linearGradient>
      <linearGradient id="swoosh-orange" x1="0" y1="0" x2="1" y2="0">
        <stop offset="0" stop-color="#e4721a"/>
        <stop offset="0.5" stop-color="#f39a1b"/>
        <stop offset="1" stop-color="#f7b833"/>
      </linearGradient>
      <radialGradient id="icon-fill" cx="0.4" cy="0.35" r="0.75">
        <stop offset="0" stop-color="#6a7178"/>
        <stop offset="1" stop-color="#3a4046"/>
      </radialGradient>
    </defs>

    <!-- white side panel -->
    <rect class="side-panel" x="0" y="0" width="1200" height="504" fill="var(--panel)"/>

    <!-- orange swoosh -->
    <path class="swoosh" d="M0,232 C180,205 360,200 560,196 C620,195 660,188 690,176 C640,212 560,226 420,236 C260,248 120,262 0,300 Z" fill="url(#swoosh-orange)"/>

    <!-- blue body wave -->
    <path class="body-wave" d="M0,292 C140,252 300,238 470,234 C600,231 680,220 740,170 C800,110 830,40 900,0 L1200,0 L1200,504 L0,504 Z" fill="url(#body-blue)"/>
    <path class="body-wave-light" d="M0,360 C220,300 420,290 620,300 C820,310 980,250 1200,150 L1200,190 C980,300 820,350 620,340 C420,330 220,340 0,410 Z" fill="var(--blue-light)" opacity="0.35"/>

    <!-- brand circle -->
    <circle class="brand-mark" cx="142" cy="140" r="52" fill="var(--blue)"/>

    <!-- icon: mobile phone -->
    <g class="icon icon-mobile">
      <circle cx="151" cy="273" r="54" fill="url(#icon-fill)" stroke="var(--icon-line)" stroke-width="5"/>
      <rect x="134" y="243" width="32" height="56" rx="5" fill="none" stroke="var(--white)" stroke-width="4"/>
      <rect x="140" y="251" width="20" height="36" fill="var(--white)" opacity="0.85"/>
      <path d="M172,246 a10,10 0 0 1 8,8 M174,238 a18,18 0 0 1 14,14" fill="none" stroke="var(--white)" stroke-width="3"/>
    </g>

    <!-- icon: keypad -->
    <g class="icon icon-keypad">
      <circle cx="290" cy="279" r="68" fill="url(#icon-fill)" stroke="var(--icon-line)" stroke-width="5"/>
      <g fill="var(--white)">
        <circle cx="266" cy="248" r="8"/><circle cx="290" cy="248" r="8"/><circle cx="314" cy="248" r="8"/>
        <circle cx="266" cy="272" r="8"/><circle cx="290" cy="272" r="8"/><circle cx="314" cy="272" r="8"/>
        <circle cx="266" cy="296" r="8"/><circle cx="290" cy="296" r="8"/><circle cx="314" cy="296" r="8"/>
        <circle cx="290" cy="320" r="8"/>
      </g>
    </g>

    <!-- icon: alarm beacon -->
    <g class="icon icon-alarm">
      <circle cx="444" cy="273" r="63" fill="url(#icon-fill)" stroke="var(--icon-line)" stroke-width="5"/>
      <path d="M418,296 L418,276 a26,26 0 0 1 52,0 L470,296 Z" fill="var(--white)"/>
      <rect x="410" y="296" width="68" height="10" rx="2" fill="var(--white)"/>
      <g stroke="var(--white)" stroke-width="5" stroke-linecap="round">
        <line x1="444" y1="228" x2="444" y2="240"/>
        <line x1="412" y1="240" x2="420" y2="249"/>
        <line x1="476" y1="240" x2="468" y2="249"/>
        <line x1="396" y1="268" x2="407" y2="270"/>
        <line x1="492" y1="268" x2="481" y2="270"/>
      </g>
    </g>

    <!-- icon: secure home -->
    <g class="icon icon-home">
      <circle cx="572" cy="251" r="56" fill="url(#icon-fill)" stroke="var(--icon-line)" stroke-width="5"/>
      <path d="M540,252 L572,222 L604,252" fill="none" stroke="var(--white)" stroke-width="5" stroke-linejoin="round"/>
      <path d="M548,248 L548,280 L596,280 L596,248" fill="none" stroke="var(--white)" stroke-width="5"/>
      <circle cx="572" cy="256" r="6" fill="var(--white)"/>
      <path d="M569,258 L566,272 L578,272 L575,258 Z" fill="var(--white)"/>
    </g>

    <!-- icon: cctv camera -->
    <g class="icon icon-cctv">
      <circle cx="667" cy="194" r="45" fill="url(#icon-fill)" stroke="var(--icon-line)" stroke-width="5"/>
      <g transform="rotate(18 667 190)">
        <rect x="638" y="178" width="50" height="20" rx="3" fill="var(--white)"/>
        <rect x="688" y="182" width="8" height="12" fill="var(--white)"/>
      </g>
      <path d="M676,208 L684,214 L684,226 M678,226 L692,226" fill="none" stroke="var(--white)" stroke-width="4"/>
    </g>
  </svg>

  <div class="brand">
    <span class="brand-line-main">KESTREL VANTAGE</span>
    <span class="brand-line-sub">SYSTEMS</span>
  </div>

  <ul class="services">
    <li>CCTV</li>
    <li>ALARMS</li>
    <li>INTERCOMS</li>
    <li>ACCESS CONTROL</li>
  </ul>

  <p class="phone">800-555-0142</p>
</main>
</body>
</html>
```